Football and sports news website

I am looking for a good design and website for a Sports news and Football website. The website will carry mainly football news from different leagues across Europe and the rest of the World. There will be a category for football, tennis, basketball, cricket,ruby. My website should be contemporary and attractive. My favorite colors are blue, purple,orange and red.
Designers can take a clue from http://varnolite.com
There will be column at the under of every news page in which readers of the article can comment.

News

Coded - Design and coding required

```html
<!DOCTYPE html>
<html lang="en">
<head>
<meta charset="utf-8">
<title>Corvel Sports – Sports News and Football</title>
<link rel="stylesheet" href="https://fonts.googleapis.com/css2?family=Open+Sans:wght@400;600;700&display=swap">
<style>
:root{
  --red:#d3202a;
  --ink:#222428;
  --text:#4a4d52;
  --muted:#8a8d92;
  --line:#e3e5e8;
  --card:#eceef1;
  --footer:#4b4e56;
  --star:#f0a21b;
  --white:#ffffff;
}
*{box-sizing:border-box;margin:0;padding:0}
html,body{width:1200px;height:3673px;overflow:hidden}
body{position:relative;background:var(--white);font-family:"Open Sans",Arial,sans-serif;color:var(--text)}
/* header */
.site-header{position:absolute;left:0;top:0;width:1200px;height:61px;background:var(--white)}
.brand{position:absolute;left:98px;top:14px;display:flex;align-items:center;gap:10px;font-size:22px;font-weight:600;color:#333}
.brand-dot{width:30px;height:30px;border-radius:50%;background:#2a7bd1}
.main-nav{position:absolute;left:400px;top:0;height:61px;display:flex;align-items:center;font-size:13px;color:#333}
.main-nav a{color:inherit;text-decoration:none;margin-right:30px}
.main-nav .sep{margin:0 10px 0 -20px;color:#666}
.btn-subscribe{position:absolute;left:963px;top:14px;width:139px;height:33px;background:var(--red);color:var(--white);font-size:13px;font-weight:600;display:flex;align-items:center;justify-content:center;border-radius:2px}
/* hero */
.hero{position:absolute;left:0;top:61px;width:1200px;height:360px;background:linear-gradient(180deg,#2c3230 0%,#4b564d 45%,#3a4a38 75%,#556b3e 100%)}
.hero-title{position:absolute;left:0;width:1200px;top:200px;text-align:center;font-size:25px;font-weight:700;color:var(--white)}
.search{position:absolute;left:184px;top:265px;width:832px;height:39px;display:flex}
.search-loc{width:208px;background:var(--white);display:flex;align-items:center;padding:0 12px;gap:8px;font-size:12px;color:#666;border-right:1px solid #ddd;justify-content:space-between}
.search-loc span{display:flex;align-items:center;gap:8px}
.search-input{width:470px;background:var(--white);display:flex;align-items:center;padding:0 16px;font-size:12px;color:#777}
.search-btn{margin-left:5px;width:149px;background:var(--red);color:var(--white);font-size:13px;font-weight:600;display:flex;align-items:center;justify-content:center;gap:8px}
.hero-dots{position:absolute;left:0;width:1200px;top:340px;display:flex;justify-content:center;gap:6px}
.hero-dots i{width:7px;height:7px;border-radius:50%;background:rgba(255,255,255,.5)}
.hero-dots i:first-child{background:var(--red)}
/* headings */
.sec-title{position:absolute;font-size:14px;font-weight:700;color:var(--ink);text-transform:uppercase}
.arrows{position:absolute;display:flex;gap:4px}
.arrows i{width:18px;height:18px;border:1px solid #ccc;display:flex;align-items:center;justify-content:center;font-style:normal;font-size:11px;color:#888}
/* sport tiles */
.tiles{position:absolute;left:100px;width:716px;display:flex;gap:20px}
.tile{width:225px;height:147px;display:flex;align-items:center;justify-content:center;color:var(--white);font-weight:700;font-size:13px;text-transform:uppercase}
/* scores */
.scores{position:absolute;left:100px;top:905px;width:255px}
.scores-sport{text-align:center;font-size:16px;color:#444;height:53px;padding-top:8px}
.league{height:293px}
.league-mark{height:66px;display:flex;align-items:center;justify-content:center;gap:7px;font-size:15px;font-weight:700;color:#1c2a55}
.league-mark b{width:12px;height:12px;background:#1c2a55;display:inline-block}
.league-name{text-align:center;font-size:11px;font-weight:700;color:#222;margin-top:4px}
.league-round{text-align:center;font-size:10px;color:var(--muted);margin-top:4px;margin-bottom:18px}
.match{height:49px;display:flex;align-items:center;border-top:1px solid var(--line);font-size:10.5px;color:#333}
.match:last-child{border-bottom:1px solid var(--line)}
.crest{width:22px;height:22px;border-radius:50%;background:#5a4aa3;flex:none}
.crest.alt{background:#555}
.crest.sq{border-radius:3px;background:#c63a2c;width:16px;height:22px}
.crest.sq.g{background:#3f8d52}
.team-a{margin-left:8px;width:72px;font-weight:600}
.time{width:62px;text-align:center;font-weight:600}
.team-b{width:68px;line-height:1.2;font-weight:600}
/* follow */
.follow{position:absolute;left:100px;top:3325px}
.small-note{font-size:10.5px;color:#555;margin-top:8px}
.socials{display:flex;gap:9px;margin-top:22px}
.socials i{width:34px;height:34px;border-radius:50%;display:block}
/* most viewed */
.mv-item{position:absolute;left:397px;width:404px;height:168px;border-bottom:1px solid var(--line);display:flex;gap:30px}
.mv-img{width:178px;height:135px;flex:none}
.mv-body{width:196px}
.mv-title{font-size:12px;font-weight:700;color:#222;line-height:1.45}
.mv-desc{font-size:11px;color:#777;line-height:1.6;margin-top:8px}
.meta{font-size:9px;color:#777;margin-top:7px;display:flex;gap:6px;align-items:center;white-space:nowrap}
.meta .st{color:var(--star);letter-spacing:1px}
.meta .ic{color:var(--star)}
/* featured */
.featured{position:absolute;left:397px;top:1523px;width:404px;display:flex;flex-direction:column;gap:37px}
.f-img{height:280px}
.f-cap{background:var(--card);padding:18px 20px 14px}
.f-title{font-size:16px;font-weight:700;color:#555;line-height:1.4}
.f-by{font-size:10.5px;color:var(--muted);margin-top:6px}
/* sidebar */
.ln1{position:absolute;left:845px;top:495px;width:257px}
.ln1-item{display:flex;gap:14px;height:59px}
.ln1-thumb{width:42px;height:42px;flex:none}
.ln1-title{font-size:10.5px;font-weight:700;color:#222;line-height:1.3}
.view-more{position:absolute;left:845px;width:257px;top:741px;text-align:right;font-size:10.5px;font-weight:700;color:var(--red)}
.ln2{position:absolute;left:845px;top:823px;width:257px}
.ln2-item{display:flex;gap:17px;height:79px}
.ln2-thumb{width:73px;height:54px;flex:none}
.ln2-title{font-size:10.5px;font-weight:700;color:#222;line-height:1.5}
.ln2 .meta{margin-top:5px}
.estab{position:absolute;left:845px;top:2216px;list-style:none;font-size:10.5px;color:#333;line-height:19.4px}
.about-img{position:absolute;left:845px;top:2581px;width:257px;height:196px}
.side-text{position:absolute;left:845px;width:257px;font-size:10.5px;color:#666;line-height:1.65}
.video{position:absolute;left:845px;top:3015px;width:257px;height:198px;display:flex;align-items:center;justify-content:center}
.play{width:50px;height:34px;background:var(--red);border-radius:8px;display:flex;align-items:center;justify-content:center}
.nl-input{position:absolute;left:845px;top:3375px;width:257px;height:34px;border:1px solid #ccc;font-size:10.5px;color:#666;display:flex;align-items:center;padding:0 10px}
.nl-btn{position:absolute;left:845px;top:3424px;width:127px;height:36px;background:var(--red);color:var(--white);font-size:11px;font-weight:700;display:flex;align-items:center;justify-content:center}
/* footer */
.site-footer{position:absolute;left:0;top:3605px;width:1200px;height:68px;background:var(--footer);display:flex;align-items:center;justify-content:center;font-size:11px;color:#c8cad0;gap:18px}
.site-footer .mark{position:absolute;right:40px;width:14px;height:14px;background:#8a8d95}
</style>
</head>
<body>

<header class="site-header">
  <div class="brand"><span class="brand-dot"></span>Corvel Sports</div>
  <nav class="main-nav">
    <a>Euro Cup</a><a>Football</a><a>All sports</a><a>Videos</a><a>More</a><a>Login</a><span class="sep">/</span><a>Register</a>
  </nav>
  <div class="btn-subscribe">Subscribe here!</div>
</header>

<section class="hero" role="img" aria-label="Stadium photo of two football players competing for the ball under floodlights">
  <h1 class="hero-title">We are a Sports news and Football</h1>
  <div class="search">
    <div class="search-loc"><span><svg width="12" height="16" viewBox="0 0 12 16"><path d="M6 0a6 6 0 0 0-6 6c0 4.5 6 10 6 10s6-5.5 6-10a6 6 0 0 0-6-6zm0 8.5A2.5 2.5 0 1 1 6 3.5a2.5 2.5 0 0 1 0 5z" fill="#f0a21b"/></svg>Location</span><svg width="9" height="6" viewBox="0 0 9 6"><path d="M1 1l3.5 3.5L8 1" stroke="#777" fill="none" stroke-width="1.5"/></svg></div>
    <div class="search-input">Search for sports</div>
    <div class="search-btn"><svg width="13" height="13" viewBox="0 0 13 13"><circle cx="5.5" cy="5.5" r="4.2" stroke="#fff" stroke-width="1.8" fill="none"/><path d="M8.6 8.6L12 12" stroke="#fff" stroke-width="1.8"/></svg>Search</div>
  </div>
  <div class="hero-dots"><i></i><i></i><i></i><i></i></div>
</section>

<h2 class="sec-title" style="left:100px;top:450px">Corvel Sports</h2>
<div class="arrows" style="left:776px;top:452px"><i>‹</i><i>›</i></div>
<div class="tiles" style="top:495px">
  <div class="tile" role="img" aria-label="Football player kicking a ball at sunset" style="background:linear-gradient(135deg,#3b2a14,#b5822f 60%,#6b4a1e)">Foot ball</div>
  <div class="tile" role="img" aria-label="Golfer swinging on a green course" style="background:linear-gradient(180deg,#9fb3c2,#6f8a5a 55%,#4d6a35)">Golf</div>
  <div class="tile" role="img" aria-label="Tennis player serving" style="background:linear-gradient(135deg,#1a1a1a,#5a4a3a 55%,#2a2420)">Tennis</div>
</div>

<h2 class="sec-title" style="left:100px;top:666px">Upcoming Sports</h2>
<div class="arrows" style="left:776px;top:668px"><i>‹</i><i>›</i></div>
<div class="tiles" style="top:703px">
  <div class="tile" role="img" aria-label="Mountain bike rider on a trail" style="background:linear-gradient(135deg,#2a2c34,#5b5f6d 60%,#3a3d47)">Cycling Mountain Bike</div>
  <div class="tile" role="img" aria-label="Sprinter on an athletics track" style="background:linear-gradient(135deg,#1f3a5a,#6a86a6 55%,#2f4a6a)">Athletics</div>
  <div class="tile" role="img" aria-label="Swimmer in a pool" style="background:linear-gradient(135deg,#0f2c4a,#3f6a9a 55%,#1d3c62)">Swimming</div>
</div>

<h2 class="sec-title" style="left:100px;top:879px">All Scores</h2>
<h2 class="sec-title" style="left:397px;top:879px">Most Viewed</h2>

<div class="scores">
  <div class="scores-sport">FOOTBALL</div>
  <div class="league"><div class="league-mark"><b></b>Continental Cup</div><div class="league-name">CONTINENTAL CUP</div><div class="league-round">Qualifying Round 1</div>
    <div class="match"><i class="crest"></i><span class="team-a">Arvashen</span><span class="time">17 : 00</span><span class="team-b">FC Vell<br>Rosa</span><i class="crest sq"></i></div>
    <div class="match"><i class="crest alt"></i><span class="team-a">Arvashen</span><span class="time">17 : 00</span><span class="team-b">FC Vell<br>Rosa</span><i class="crest sq"></i></div>
    <div class="match"><i class="crest alt"></i><span class="team-a">Arvashen</span><span class="time">17 : 00</span><span class="team-b">FC Vell<br>Rosa</span><i class="crest sq g"></i></div>
  </div>
  <div class="league"><div class="league-mark"><b></b>Stride Athletics</div><div class="league-name">CONTINENTAL CUP</div><div class="league-round">Qualifying Round 1</div>
    <div class="match"><i class="crest"></i><span class="team-a">Arvashen</span><span class="time">17 : 00</span><span class="team-b">FC Vell<br>Rosa</span><i class="crest sq"></i></div>
    <div class="match"><i class="crest alt"></i><span class="team-a">Arvashen</span><span class="time">17 : 00</span><span class="team-b">FC Vell<br>Rosa</span><i class="crest sq"></i></div>
    <div class="match"><i class="crest alt"></i><span class="team-a">Arvashen</span><span class="time">17 : 00</span><span class="team-b">FC Vell<br>Rosa</span><i class="crest sq g"></i></div>
  </div>
  <div class="league"><div class="league-mark"><b></b>Norda Sports</div><div class="league-name">CONTINENTAL CUP</div><div class="league-round">Qualifying Round 1</div>
    <div class="match"><i class="crest"></i><span class="team-a">Arvashen</span><span class="time">17 : 00</span><span class="team-b">FC Vell<br>Rosa</span><i class="crest sq"></i></div>
    <div class="match"><i class="crest alt"></i><span class="team-a">Arvashen</span><span class="time">17 : 00</span><span class="team-b">FC Vell<br>Rosa</span><i class="crest sq"></i></div>
    <div class="match"><i class="crest alt"></i><span class="team-a">Arvashen</span><span class="time">17 : 00</span><span class="team-b">FC Vell<br>Rosa</span><i class="crest sq g"></i></div>
  </div>
  <div class="league"><div class="league-mark"><b></b>Norda Sports</div><div class="league-name">CONTINENTAL CUP</div><div class="league-round">Qualifying Round 1</div>
    <div class="match"><i class="crest"></i><span class="team-a">Arvashen</span><span class="time">17 : 00</span><span class="team-b">FC Vell<br>Rosa</span><i class="crest sq"></i></div>
    <div class="match"><i class="crest alt"></i><span class="team-a">Arvashen</span><span class="time">17 : 00</span><span class="team-b">FC Vell<br>Rosa</span><i class="crest sq"></i></div>
    <div class="match"><i class="crest alt"></i><span class="team-a">Arvashen</span><span class="time">17 : 00</span><span class="team-b">FC Vell<br>Rosa</span><i class="crest sq g"></i></div>
  </div>
  <div class="league"><div class="league-mark"><b></b>Pellow Sport</div><div class="league-name">CONTINENTAL CUP</div><div class="league-round">Qualifying Round 1</div>
    <div class="match"><i class="crest"></i><span class="team-a">Arvashen</span><span class="time">17 : 00</span><span class="team-b">FC Vell<br>Rosa</span><i class="crest sq"></i></div>
    <div class="match"><i class="crest alt"></i><span class="team-a">Arvashen</span><span class="time">17 : 00</span><span class="team-b">FC Vell<br>Rosa</span><i class="crest sq"></i></div>
    <div class="match"><i class="crest alt"></i><span class="team-a">Arvashen</span><span class="time">17 : 00</span><span class="team-b">FC Vell<br>Rosa</span><i class="crest sq g"></i></div>
  </div>
  <div class="league"><div class="league-mark"><b></b>Quarry Sports</div><div class="league-name">CONTINENTAL CUP</div><div class="league-round">Qualifying Round 1</div>
    <div class="match"><i class="crest"></i><span class="team-a">Arvashen</span><span class="time">17 : 00</span><span class="team-b">FC Vell<br>Rosa</span><i class="crest sq"></i></div>
    <div class="match"><i class="crest alt"></i><span class="team-a">Arvashen</span><span class="time">17 : 00</span><span class="team-b">FC Vell<br>Rosa</span><i class="crest sq"></i></div>
    <div class="match"><i class="crest alt"></i><span class="team-a">Arvashen</span><span class="time">17 : 00</span><span class="team-b">FC Vell<br>Rosa</span><i class="crest sq g"></i></div>
  </div>
  <div class="league"><div class="league-mark"><b></b>Tessel Sports</div><div class="league-name">CONTINENTAL CUP</div><div class="league-round">Qualifying Round 1</div>
    <div class="match"><i class="crest"></i><span class="team-a">Arvashen</span><span class="time">17 : 00</span><span class="team-b">FC Vell<br>Rosa</span><i class="crest sq"></i></div>
    <div class="match"><i class="crest alt"></i><span class="team-a">Arvashen</span><span class="time">17 : 00</span><span class="team-b">FC Vell<br>Rosa</span><i class="crest sq"></i></div>
    <div class="match"><i class="crest alt"></i><span class="team-a">Arvashen</span><span class="time">17 : 00</span><span class="team-b">FC Vell<br>Rosa</span><i class="crest sq g"></i></div>
  </div>
  <div class="league"><div class="league-mark"><b></b>Ridgebacks</div><div class="league-name">CONTINENTAL CUP</div><div class="league-round">Qualifying Round 1</div>
    <div class="match"><i class="crest"></i><span class="team-a">Arvashen</span><span class="time">17 : 00</span><span class="team-b">FC Vell<br>Rosa</span><i class="crest sq"></i></div>
    <div class="match"><i class="crest alt"></i><span class="team-a">Arvashen</span><span class="time">17 : 00</span><span class="team-b">FC Vell<br>Rosa</span><i class="crest sq"></i></div>
    <div class="match"><i class="crest alt"></i><span class="team-a">Arvashen</span><span class="time">17 : 00</span><span class="team-b">FC Vell<br>Rosa</span><i class="crest sq g"></i></div>
  </div>
</div>

<div class="follow">
  <h2 class="sec-title" style="position:static">Follow Us</h2>
  <p class="small-note">Connect with our social network</p>
  <div class="socials"><i style="background:#3b5998"></i><i style="background:#0e76a8"></i><i style="background:#f7931e"></i><i style="background:#29a9e1"></i><i style="background:#d8261f"></i></div>
</div>

<article class="mv-item" style="top:921px">
  <div class="mv-img" role="img" aria-label="Player striking a fiery football" style="background:linear-gradient(135deg,#2a0f08,#c2461a 55%,#3a1a10)"></div>
  <div class="mv-body"><h3 class="mv-title">Lorem Ipsum is simply dummy text of the printing</h3><p class="mv-desc">Lorem Ipsum is simply dummy text of the printing and typesetting industry. Lorem Ipsum has been the industry</p><div class="meta"><span class="ic">♟</span>120 reviews <span class="ic">♥</span>180 Likes <span class="st">★★★★☆</span></div></div>
</article>
<article class="mv-item" style="top:1107px">
  <div class="mv-img" role="img" aria-label="Two players tackling on grass" style="background:linear-gradient(135deg,#2f6a2a,#5aa03c 55%,#2e5a26)"></div>
  <div class="mv-body"><h3 class="mv-title">Lorem Ipsum is simply dummy text of the printing</h3><p class="mv-desc">Lorem Ipsum is simply dummy text of the printing and typesetting industry. Lorem Ipsum has been the industry</p><div class="meta"><span class="ic">♟</span>120 reviews <span class="ic">♥</span>180 Likes <span class="st">★★★★☆</span></div></div>
</article>
<article class="mv-item" style="top:1293px">
  <div class="mv-img" role="img" aria-label="Goalkeeper diving for a ball" style="background:linear-gradient(135deg,#2d3a1a,#7a8a3a 55%,#3a4a20)"></div>
  <div class="mv-body"><h3 class="mv-title">Lorem Ipsum is simply dummy text of the printing</h3><p class="mv-desc">Lorem Ipsum is simply dummy text of the printing and typesetting industry. Lorem Ipsum has been the industry</p><div class="meta"><span class="ic">♟</span>120 reviews <span class="ic">♥</span>180 Likes <span class="st">★★★★☆</span></div></div>
</article>

<h2 class="sec-title" style="left:397px;top:1484px">Featured</h2>
<div class="featured">
  <article><div class="f-img" role="img" aria-label="Footballers jumping for a header in a floodlit stadium" style="background:linear-gradient(180deg,#1c2228,#45504a 50%,#3d6a2c)"></div><div class="f-cap"><h3 class="f-title">What now for Dane Holloway?</h3><p class="f-by">By Rhea Voss • 24 minutes ago</p></div></article>
  <article><div class="f-img" role="img" aria-label="American football players colliding on a field" style="background:linear-gradient(180deg,#3a5a2a,#5f8f3a 55%,#467a2c)"></div><div class="f-cap"><h3 class="f-title">Paper Round: Ferrante attempts to lure Okonde to Northgate</h3><p class="f-by">By Rhea Voss • 24 minutes ago</p></div></article>
  <article><div class="f-img" role="img" aria-label="Goalkeeper in yellow diving to save a shot" style="background:linear-gradient(180deg,#6a6a6a,#9a9488 50%,#5a6a3a)"></div><div class="f-cap"><h3 class="f-title">What now for Dane Holloway?</h3><p class="f-by">By Rhea Voss • 24 minutes ago</p></div></article>
  <article><div class="f-img" role="img" aria-label="Player kicking a ball mid-air in a stadium" style="background:linear-gradient(180deg,#1c2a40,#4a6a8a 50%,#2a3a4a)"></div><div class="f-cap"><h3 class="f-title">Paper Round: Ferrante attempts to lure Okonde to Northgate</h3><p class="f-by">By Rhea Voss • 24 minutes ago</p></div></article>
  <article><div class="f-img" role="img" aria-label="Rugby scrum in muddy kits" style="background:linear-gradient(180deg,#9aa0a4,#7a6a5a 55%,#5a4a3a)"></div><div class="f-cap"><h3 class="f-title">Paper Round: Ferrante attempts to lure Okonde to Northgate</h3><p class="f-by">By Rhea Voss • 24 minutes ago</p></div></article>
</div>

<h2 class="sec-title" style="left:845px;top:450px">Latest News</h2>
<div class="ln1">
  <div class="ln1-item"><div class="ln1-thumb" role="img" aria-label="Football action" style="background:linear-gradient(135deg,#333,#6a7a4a)"></div><div><h3 class="ln1-title">Lorem Ipsum is simply dummy</h3><div class="meta"><span class="ic">♟</span>120 reviews <span class="ic">♥</span>180 Likes <span class="st">★★★★☆</span></div></div></div>
  <div class="ln1-item"><div class="ln1-thumb" role="img" aria-label="Football action" style="background:linear-gradient(135deg,#2a3a5a,#7a8aa0)"></div><div><h3 class="ln1-title">Lorem Ipsum is simply dummy</h3><div class="meta"><span class="ic">♟</span>120 reviews <span class="ic">♥</span>180 Likes <span class="st">★★★★☆</span></div></div></div>
  <div class="ln1-item"><div class="ln1-thumb" role="img" aria-label="Football action" style="background:linear-gradient(135deg,#5a3a2a,#a07a5a)"></div><div><h3 class="ln1-title">Lorem Ipsum is simply dummy</h3><div class="meta"><span class="ic">♟</span>120 reviews <span class="ic">♥</span>180 Likes <span class="st">★★★★☆</span></div></div></div>
  <div class="ln1-item"><div class="ln1-thumb" role="img" aria-label="Football action" style="background:linear-gradient(135deg,#1a2a4a,#3a6aa0)"></div><div><h3 class="ln1-title">Lorem Ipsum is simply dummy</h3><div class="meta"><span class="ic">♟</span>120 reviews <span class="ic">♥</span>180 Likes <span class="st">★★★★☆</span></div></div></div>
</div>
<div class="view-more">View more news ❯</div>

<h2 class="sec-title" style="left:845px;top:781px">Latest News</h2>
<div class="ln2">
  <div class="ln2-item"><div class="ln2-thumb" role="img" aria-label="Sports photo" style="background:linear-gradient(135deg,#222,#556)"></div><div><h3 class="ln2-title">Lorem Ipsum is simply dummy text of the printing</h3><div class="meta"><span class="ic">◷</span>10 h &nbsp; Tennis</div></div></div>
  <div class="ln2-item"><div class="ln2-thumb" role="img" aria-label="Sports photo" style="background:linear-gradient(135deg,#3a5a2a,#7a9a5a)"></div><div><h3 class="ln2-title">Lorem Ipsum is simply dummy text of the printing</h3><div class="meta"><span class="ic">◷</span>10 h &nbsp; Tennis</div></div></div>
  <div class="ln2-item"><div class="ln2-thumb" role="img" aria-label="Sports photo" style="background:linear-gradient(135deg,#4a2a1a,#9a5a3a)"></div><div><h3 class="ln2-title">Lorem Ipsum is simply dummy text of the printing</h3><div class="meta"><span class="ic">◷</span>10 h &nbsp; Tennis</div></div></div>
  <div class="ln2-item"><div class="ln2-thumb" role="img" aria-label="Sports photo" style="background:linear-gradient(135deg,#1a3a5a,#5a8ab0)"></div><div><h3 class="ln2-title">Lorem Ipsum is simply dummy text of the printing</h3><div class="meta"><span class="ic">◷</span>10 h &nbsp; Tennis</div></div></div>
  <div class="ln2-item"><div class="ln2-thumb" role="img" aria-label="Sports photo" style="background:linear-gradient(135deg,#5a2a2a,#a04a3a)"></div><div><h3 class="ln2-title">Lorem Ipsum is simply dummy text of the printing</h3><div class="meta"><span class="ic">◷</span>10 h &nbsp; Tennis</div></div></div>
  <div class="ln2-item"><div class="ln2-thumb" role="img" aria-label="Sports photo" style="background:linear-gradient(135deg,#2a2a3a,#6a6a8a)"></div><div><h3 class="ln2-title">Lorem Ipsum is simply dummy text of the printing</h3><div class="meta"><span class="ic">◷</span>10 h &nbsp; Tennis</div></div></div>
  <div class="ln2-item"><div class="ln2-thumb" role="img" aria-label="Sports photo" style="background:linear-gradient(135deg,#1a2a3a,#4a6a7a)"></div><div><h3 class="ln2-title">Lorem Ipsum is simply dummy text of the printing</h3><div class="meta"><span class="ic">◷</span>10 h &nbsp; Tennis</div></div></div>
  <div class="ln2-item"><div class="ln2-thumb" role="img" aria-label="Sports photo" style="background:linear-gradient(135deg,#2a4a6a,#6a9ac0)"></div><div><h3 class="ln2-title">Lorem Ipsum is simply dummy text of the printing</h3><div class="meta"><span class="ic">◷</span>10 h &nbsp; Tennis</div></div></div>
  <div class="ln2-item"><div class="ln2-thumb" role="img" aria-label="Sports photo" style="background:linear-gradient(135deg,#2a3a2a,#5a7a4a)"></div><div><h3 class="ln2-title">Lorem Ipsum is simply dummy text of the printing</h3><div class="meta"><span class="ic">◷</span>10 h &nbsp; Tennis</div></div></div>
  <div class="ln2-item"><div class="ln2-thumb" role="img" aria-label="Sports photo" style="background:linear-gradient(135deg,#3a5a2a,#8aaa5a)"></div><div><h3 class="ln2-title">Lorem Ipsum is simply dummy text of the printing</h3><div class="meta"><span class="ic">◷</span>10 h &nbsp; Tennis</div></div></div>
  <div class="ln2-item"><div class="ln2-thumb" role="img" aria-label="Sports photo" style="background:linear-gradient(135deg,#1a1a2a,#4a4a6a)"></div><div><h3 class="ln2-title">Lorem Ipsum is simply dummy text of the printing</h3><div class="meta"><span class="ic">◷</span>10 h &nbsp; Tennis</div></div></div>
  <div class="ln2-item"><div class="ln2-thumb" role="img" aria-label="Sports photo" style="background:linear-gradient(135deg,#4a3a2a,#9a7a5a)"></div><div><h3 class="ln2-title">Lorem Ipsum is simply dummy text of the printing</h3><div class="meta"><span class="ic">◷</span>10 h &nbsp; Tennis</div></div></div>
  <div class="ln2-item"><div class="ln2-thumb" role="img" aria-label="Sports photo" style="background:linear-gradient(135deg,#5a4a2a,#aa8a4a)"></div><div><h3 class="ln2-title">Lorem Ipsum is simply dummy text of the printing</h3><div class="meta"><span class="ic">◷</span>10 h &nbsp; Tennis</div></div></div>
  <div class="ln2-item"><div class="ln2-thumb" role="img" aria-label="Sports photo" style="background:linear-gradient(135deg,#1a2a1a,#4a6a3a)"></div><div><h3 class="ln2-title">Lorem Ipsum is simply dummy text of the printing</h3><div class="meta"><span class="ic">◷</span>10 h &nbsp; Tennis</div></div></div>
  <div class="ln2-item"><div class="ln2-thumb" role="img" aria-label="Sports photo" style="background:linear-gradient(135deg,#3a2a2a,#7a4a4a)"></div><div><h3 class="ln2-title">Lorem Ipsum is simply dummy text of the printing</h3><div class="meta"><span class="ic">◷</span>10 h &nbsp; Tennis</div></div></div>
  <div class="ln2-item"><div class="ln2-thumb" role="img" aria-label="Sports photo" style="background:linear-gradient(135deg,#1a3a6a,#4a7ab0)"></div><div><h3 class="ln2-title">Lorem Ipsum is simply dummy text of the printing</h3><div class="meta"><span class="ic">◷</span>10 h &nbsp; Tennis</div></div></div>
  <div class="ln2-item"><div class="ln2-thumb" role="img" aria-label="Sports photo" style="background:linear-gradient(135deg,#2a2a4a,#5a5a9a)"></div><div><h3 class="ln2-title">Lorem Ipsum is simply dummy text of the printing</h3><div class="meta"><span class="ic">◷</span>10 h &nbsp; Tennis</div></div></div>
</div>

<h2 class="sec-title" style="left:845px;top:2177px">Establishments</h2>
<ul class="estab">
  <li>Cycling Road</li><li>Cycling Track</li><li>Diving</li><li>Equestrian</li><li>Fencing</li><li>Football</li><li>Golf</li><li>Handball</li><li>Hockey</li><li>Judo</li><li>Marathon Swimming</li><li>Modern Pentathlon</li><li>Rhythmic Gymnastics</li><li>Rowing</li>
</ul>

<h2 class="sec-title" style="left:845px;top:2539px">About Corvel Sports</h2>
<div class="about-img" role="img" aria-label="Footballer in red controlling the ball on a pitch" style="background:linear-gradient(180deg,#3a3a2a,#7a7a4a 50%,#4a6a2a)"></div>
<p class="side-text" style="top:2796px">Lorem Ipsum is simply dummy text of the printing and typesetting industry. Lorem Ipsum has been the industry's standard dummy text ever since the 1500s, when an unknown printer took a galley of type and scrambled it to make a type specimen book. It has survived not only five centuries...</p>

<h2 class="sec-title" style="left:845px;top:2975px">Recent Videos</h2>
<div class="video" role="img" aria-label="Video still of a player kicking a ball in a night stadium" style="background:linear-gradient(180deg,#1a2030,#3a4a5a 55%,#2a4a2a)">
  <div class="play"><svg width="14" height="16" viewBox="0 0 14 16"><path d="M0 0l14 8-14 8z" fill="#fff"/></svg></div>
</div>
<p class="side-text" style="top:3237px">Lorem Ipsum is simply dummy text of the printing and typesetting industry...</p>

<h2 class="sec-title" style="left:845px;top:3311px">Newsletter Signup</h2>
<p class="side-text" style="top:3340px;color:#555">Connect with our social network</p>
<div class="nl-input">Enter your email id</div>
<div class="nl-btn">SUBSCRIBE</div>

<footer class="site-footer">
  <span>© 2016, Fieldline Studio. All rights reserved.</span><span>Terms &amp; Conditions</span><span>/</span><span>Privacy Policy</span><span>/</span><span>Disclaimer</span><span>/</span><span>Sitemap</span>
  <i class="mark"></i>
</footer>

</body>
</html>
```